Law Firm Needs Brochure Redesign Using New Logo

We are a personal injury law firm that does auto injuries and other personal injury cases. We want a new brochure that has our updated logo and information. Instead of gold and black, we want more navy, as matches the new logo. The Auto Liability portion should read: "(required by the state of Arizona in the amounts of $25,000 per person / $50,000 per accident, but a higher amount may be best )." The other information can remain the same. We'd like the brochure to keep the same professional tone as the previous brochure.
Our website is https://www.marbrenlegal.com/.

```html
<!DOCTYPE html>
<html lang="en">
<head>
<meta charset="utf-8">
<title>Marbren Legal – Car Accident Brochure</title>
<link href="https://fonts.googleapis.com/css2?family=Montserrat:wght@400;500;600;700;800&display=swap" rel="stylesheet">
<style>
  :root {
    --navy: #172649;
    --navy-deep: #121f3d;
    --paper: #f3f3f5;
    --white: #ffffff;
    --ink: #1b2a4e;
    --muted: #56607a;
    --backdrop: #d9dadc;
  }
  * { box-sizing: border-box; margin: 0; padding: 0; }
  html, body { width: 1200px; height: 900px; overflow: hidden; }
  body {
    background: var(--backdrop);
    font-family: "Montserrat", sans-serif;
    color: var(--ink);
    position: relative;
  }
  .spread {
    position: absolute;
    top: 237px;
    width: 585px;
    height: 426px;
    display: flex;
    box-shadow: 0 10px 30px rgba(0,0,0,.18);
  }
  .spread--outside { left: 10px; }
  .spread--inside { left: 605px; }
  .panel { position: relative; width: 195px; height: 100%; overflow: hidden; }
  .panel--navy { background: var(--navy); color: var(--white); }
  .panel--paper { background: var(--paper); }
  .panel--white { background: var(--white); }

  /* brand lockup */
  .lockup { display: flex; align-items: center; gap: 5px; font-weight: 700; letter-spacing: .06em; text-transform: uppercase; white-space: nowrap; }
  .lockup__dot { border-radius: 50%; flex: none; }
  .lockup--light { color: var(--white); }
  .lockup--light .lockup__dot { background: var(--white); }
  .lockup--dark { color: var(--navy); }
  .lockup--dark .lockup__dot { background: var(--navy); }

  /* photo placeholders */
  .photo { position: absolute; }
  .photo--wheel { inset: 0 0 100px 0; background: linear-gradient(160deg, #22355e 0%, #1a2a50 55%, #14213f 100%); }
  .photo--car { left: 0; top: 0; width: 195px; height: 243px; border-bottom-right-radius: 24px; border-bottom: 4px solid var(--white);
    background: linear-gradient(180deg, #5d6b80 0%, #8a939c 30%, #4d5560 55%, #23272d 80%, #3b3f44 100%); }
  .photo--crash { left: 6px; top: 247px; width: 189px; height: 179px; border-top-left-radius: 30px;
    border-top: 5px solid var(--navy); border-left: 5px solid var(--navy);
    background: linear-gradient(160deg, #9a9c9f 0%, #6e6a66 40%, #a6743f 70%, #5b4330 100%); }
  .photo--driver { left: 5px; top: 243px; width: 190px; height: 183px; border-top-left-radius: 30px;
    border-top: 5px solid var(--navy); border-left: 5px solid var(--navy);
    background: linear-gradient(150deg, #d9dde2 0%, #aeb4bb 35%, #4f6c92 65%, #2f3640 100%); }
  .photo--hands { left: 6px; top: 0; width: 183px; height: 288px; border-radius: 0 0 28px 28px;
    background: linear-gradient(180deg, #f4f5f6 0%, #e6e3df 45%, #d9c4b2 75%, #ecebea 100%); }

  /* stats panel */
  .stats { position: absolute; left: 16px; top: 24px; width: 166px; height: 150px; border-radius: 16px; background: rgba(255,255,255,.12); text-align: center; padding-top: 10px; }
  .stats__over { font-size: 9px; letter-spacing: .04em; }
  .stats__num { font-size: 29px; font-weight: 700; line-height: 1; margin: 1px 0 3px; }
  .stats__cap { font-size: 6.8px; line-height: 1.2; margin-bottom: 7px; padding: 0 8px; }
  .pitch { position: absolute; left: 12px; right: 12px; top: 188px; font-size: 7px; line-height: 1.4; text-align: center; }
  .pitch p + p { margin-top: 7px; }
  .upper-curve { position: absolute; left: 0; top: 0; width: 195px; height: 330px; border-bottom-right-radius: 40px; border-bottom: 4px solid var(--white); border-right: 4px solid var(--white); }
  .visit { position: absolute; left: 0; right: 0; top: 346px; text-align: center; }
  .visit__label { font-size: 11px; font-weight: 800; }
  .visit__url { font-size: 11px; letter-spacing: .22em; margin-top: 5px; }
  .visit .lockup { justify-content: center; font-size: 7px; margin-top: 12px; }
  .visit .lockup__dot { width: 9px; height: 9px; }

  /* contact panel */
  .contact { position: absolute; left: 0; right: 0; top: 26px; text-align: center; }
  .contact__mark { width: 34px; height: 34px; border-radius: 50%; background: var(--navy); margin: 0 auto 14px; }
  .contact__kicker { font-size: 6.5px; font-weight: 600; color: var(--muted); }
  .contact__title { font-size: 18px; font-weight: 800; color: var(--navy); line-height: 1.05; }
  .contact__rule { width: 22px; height: 2px; background: var(--navy); margin: 5px auto 12px; }
  .contact__item { margin-bottom: 10px; font-size: 5px; letter-spacing: .05em; color: var(--muted); text-transform: uppercase; line-height: 1.3; }
  .contact__icon { width: 13px; height: 13px; border-radius: 50%; background: var(--navy); margin: 0 auto 4px; display: flex; align-items: center; justify-content: center; }

  /* cover headline */
  .cover-lockup { position: absolute; left: 0; right: 0; top: 22px; justify-content: center; font-size: 10px; }
  .cover-lockup .lockup__dot { width: 14px; height: 14px; }
  .headline { position: absolute; left: 16px; top: 268px; border-left: 2px solid var(--white); padding-left: 8px; }
  .headline__lead { font-size: 10px; line-height: 1.15; }
  .headline__main { font-size: 17.5px; font-weight: 800; line-height: 1.2; margin: 1px 0; }
  .headline strong { font-weight: 800; }
  .dots { position: absolute; display: grid; grid-template-columns: repeat(6, 2px); gap: 6px 7px; }
  .dots span { width: 2px; height: 2px; border-radius: 50%; background: currentColor; }
  .dots--cover { right: 14px; bottom: 14px; color: var(--white); }

  /* tips panel */
  .tips { position: absolute; left: 10px; right: 10px; top: 14px; }
  .tips__title { font-size: 9.5px; font-weight: 600; margin-bottom: 6px; }
  .tips__list { list-style: none; counter-reset: tip; }
  .tips__list li { counter-increment: tip; position: relative; padding-left: 9px; font-size: 5.6px; line-height: 1.22; margin-bottom: 5px; }
  .tips__list li::before { content: counter(tip) "."; position: absolute; left: 0; top: -.5px; font-weight: 700; font-size: 6px; }
  .tips-band .lockup { position: absolute; left: 0; right: 0; top: 378px; justify-content: center; font-size: 9px; }
  .tips-band .lockup__dot { width: 14px; height: 14px; }
  .tips-curve { position: absolute; left: 0; top: 0; width: 195px; height: 344px; border-bottom-right-radius: 36px; border-bottom: 4px solid var(--white); border-right: 4px solid var(--white); }

  /* coverage panel */
  .coverage { position: absolute; left: 9px; right: 9px; top: 18px; }
  .coverage__title { font-size: 15px; font-weight: 700; color: var(--navy); line-height: 1.15; margin-bottom: 9px; }
  .coverage p { font-size: 5.6px; line-height: 1.3; color: var(--muted); margin-bottom: 7px; }
  .coverage b { color: var(--navy); font-weight: 700; }
  .dots--coverage { right: 10px; top: 18px; color: var(--navy); gap: 5px 5px; }

  /* safety panel */
  .safety { position: absolute; left: 8px; right: 8px; top: 306px; }
  .safety h3 { font-size: 8.5px; font-weight: 700; letter-spacing: .02em; margin-bottom: 3px; }
  .safety p { font-size: 5.8px; line-height: 1.3; margin-bottom: 9px; }
</style>
</head>
<body>

<!-- Outside spread -->
<section class="spread spread--outside" aria-label="Brochure outside">
  <article class="panel panel--navy">
    <div class="photo photo--wheel" role="img" aria-label="Dark close-up of a car wheel and fender tinted navy"></div>
    <div class="upper-curve"></div>
    <div class="stats">
      <p class="stats__over">OVER</p>
      <p class="stats__num">107,000</p>
      <p class="stats__cap">Crashes Will Happen In The State Of Arizona This Year.</p>
      <p class="stats__over">OVER</p>
      <p class="stats__num">700</p>
      <p class="stats__cap">Of Them Will Result In Fatalities</p>
    </div>
    <div class="pitch">
      <p>If we don't win, you don't pay attorney fees. That seems fair to us. Know what's happening with your</p>
      <p>case, get the answers to your questions and work on getting better with the confidence that you've got an excellent group of people working for you.</p>
    </div>
    <div class="visit">
      <p class="visit__label">Visit Now</p>
      <p class="visit__url">MarbrenLegal.com</p>
      <div class="lockup lockup--light"><span class="lockup__dot"></span>Marbren Legal</div>
    </div>
  </article>

  <article class="panel panel--paper">
    <div class="contact">
      <div class="contact__mark"></div>
      <p class="contact__kicker">Get in touch</p>
      <h2 class="contact__title">Contact</h2>
      <div class="contact__rule"></div>
      <div class="contact__item">
        <div class="contact__icon"><svg width="7" height="7" viewBox="0 0 10 10"><path d="M1 1 L9 5 L5 6 L4 9 Z" fill="#fff"/></svg></div>
        info@marbrenlegal.com
      </div>
      <div class="contact__item">
        <div class="contact__icon"><svg width="7" height="7" viewBox="0 0 10 10"><path d="M2 1 L4 1 L5 3.5 L3.8 4.5 Q5 6.5 5.5 6.2 L6.5 5 L9 6 L9 8 Q8 9.5 6 8.5 Q2 6.5 1 3 Q1 1.5 2 1Z" fill="#fff"/></svg></div>
        602.555.0147
      </div>
      <div class="contact__item">
        <div class="contact__icon"><svg width="7" height="7" viewBox="0 0 10 10"><path d="M5 0.5 A3.3 3.3 0 0 1 8.3 3.8 Q8.3 6 5 9.5 Q1.7 6 1.7 3.8 A3.3 3.3 0 0 1 5 0.5Z" fill="#fff"/><circle cx="5" cy="3.8" r="1.3" fill="#172649"/></svg></div>
        4870 N. Cedar Ridge Road Suite B110<br>Phoenix AZ 85016
      </div>
    </div>
    <div class="photo photo--crash" role="img" aria-label="Motorcycle lying on the road after a collision with a car"></div>
  </article>

  <article class="panel panel--navy">
    <div class="photo photo--car" role="img" aria-label="Black sedan parked on a road with mountains and a dusk sky behind"></div>
    <div class="lockup lockup--dark cover-lockup"><span class="lockup__dot"></span>Marbren Legal</div>
    <div class="headline">
      <p class="headline__lead">Protect Your<br>Family In Case Of A</p>
      <p class="headline__main">Car Accident</p>
      <p class="headline__lead">A Little Knowledge<br>And <strong>Preparation Go</strong><br><strong>A Long Way</strong></p>
    </div>
    <div class="dots dots--cover"><span></span><span></span><span></span><span></span><span></span><span></span><span></span><span></span><span></span><span></span><span></span><span></span></div>
  </article>
</section>

<!-- Inside spread -->
<section class="spread spread--inside" aria-label="Brochure inside">
  <article class="panel panel--navy tips-band">
    <div class="tips-curve"></div>
    <div class="tips">
      <h2 class="tips__title">Top 10 Tips to Avoid a Crash</h2>
      <ol class="tips__list">
        <li>Anyone making a left turn must wait for all oncoming traffic to clear before proceeding. Yes, even if the light has turned yellow. Wait to be sure that all traffic has stopped.</li>
        <li>When your light turns green, check to be sure that no vehicles are entering the intersection late.</li>
        <li>Allow plenty of room between you and the car in front of you. Traffic can stop in an instant, even if you can't see anything ahead.</li>
        <li>Avoid being distracted. Teenagers are especially susceptible to losing focus if there are too many friends in the car.</li>
        <li>Keep the volume of your radio down and never wear headphones. Cars are very soundproof these days, but you need to be able to hear an ambulance or police siren.</li>
        <li>Be especially careful on the weekends and early morning hours.</li>
        <li>Don't speed. Speed is a factor in most crashes. Street lights are timed and the freeway has traffic. It's likely you won't get there much faster even if you do speed.</li>
        <li>Don't drink and drive. Many cab companies offer a free service to get you home safe.</li>
        <li>Use your turn signals. This gives an early warning to vehicles you may not be able to see.</li>
      </ol>
    </div>
    <div class="lockup lockup--light"><span class="lockup__dot"></span>Marbren Legal</div>
  </article>

  <article class="panel panel--white">
    <div class="dots dots--coverage"><span></span><span></span><span></span><span></span><span></span><span></span><span></span><span></span><span></span><span></span><span></span><span></span></div>
    <div class="coverage">
      <h2 class="coverage__title">Have the<br>Right Coverage</h2>
      <p>Many people don't know about the different kinds of insurance available. In addition to health insurance, we suggest:</p>
      <p><b>Auto Liability</b> (required by the state of Arizona in the <b>amounts of $25,000 per person / $50,000 per accident</b>, but a higher amount may be best )</p>
      <p><b>Uninsured or Underinsured Motorist Coverage.</b> This protects YOU when the other driver doesn't have insurance or not enough.</p>
      <p><b>Medical Payments Coverage.</b> Up to $5,000 in coverage will be paid out to you no matter who is at fault in an accident and does not need to be reimbursed.</p>
      <p><b>Homeowners / Renters Insurance.</b> Protects you in case of injuries on your property as well as damage to your home from covered events.</p>
    </div>
    <div class="photo photo--driver" role="img" aria-label="Man in a denim shirt fastening his seatbelt in the driver's seat"></div>
  </article>

  <article class="panel panel--navy">
    <div class="photo photo--hands" role="img" aria-label="Two hands sheltering a small car icon against a white background"></div>
    <div class="safety">
      <h3>MODEL SAFE BEHAVIOR</h3>
      <p>Always buckle up. Always put your children in car seats/boosters that are rated for their height and weight.</p>
      <h3>NEVER TEXT WHILE DRIVING</h3>
      <p>Studies have shown that texting while driving is as dangerous as driving intoxicated. Show your children that no text is more important than your safety. It can wait.</p>
    </div>
  </article>
</section>

</body>
</html>
```